bluefinwardco.com website design

We're looking for a website design for Bluefinwardco.com .
Bluefinward is a manufacturer of high visibility traffic safety equipment and gear.. Our initial site will be a product catalog site featuring traffic cones . We will eventually expand to include traffic barriers, mesh signs, safety clothing and more. Our logo and product pictures can be found at bluefinwardco.com .
Updates

Need extra days to review

Target Market(s)

We service a wide range of customers with our focus markets being construction, manufacturing and municipalities.

Industry/Entity Type

Safety Products

Number of Pages Required

1 page

Font styles to use
Sans Serif

Requirements
Must have
• company logo w/compatible color scheme

```html
<!DOCTYPE html>
<html lang="en">
<head>
<meta charset="utf-8">
<title>Bluefinward Safety Products</title>
<link href="https://fonts.googleapis.com/css2?family=Poppins:wght@400;500;600;700&display=swap" rel="stylesheet">
<style>
:root{
  --orange:#ee8f35;
  --orange-dark:#e07a1c;
  --green:#6daf55;
  --green-pill:#5cb04a;
  --yellow:#f5d53a;
  --ink:#2b2b2b;
  --muted:#6b6b6b;
  --line:#e3e3e3;
  --peach:#fae6d6;
  --footer:#262626;
  --white:#ffffff;
}
*{box-sizing:border-box;margin:0;padding:0}
html,body{width:1200px;height:4219px;overflow:hidden}
body{font-family:"Poppins",sans-serif;color:var(--ink);background:var(--white);position:relative}
.abs{position:absolute}
.accent{color:var(--orange)}
.btn{position:absolute;display:flex;align-items:center;justify-content:center;background:var(--orange);color:var(--white);font-weight:600;border-radius:4px}

/* header */
.site-header{position:absolute;left:0;top:0;width:1200px;height:105px;background:var(--white)}
.logo{position:absolute;display:flex;align-items:center;gap:8px}
.logo-mark{width:30px;height:30px;border-radius:50%;background:var(--orange)}
.logo-name{font-weight:600;color:var(--orange);font-size:26px;line-height:1}
.logo-sub{font-size:12px;font-weight:600;color:var(--ink);display:block;margin-top:2px;text-align:right}
.search{left:566px;top:10px;width:364px;height:34px;border:1px solid var(--line);border-radius:3px;font-size:10px;color:#999;padding:9px 22px}
.nav a{position:absolute;top:70px;font-size:12px;font-weight:500;color:var(--ink);text-decoration:none}
.nav .active::after{content:"";position:absolute;left:-10px;right:-10px;top:-17px;height:2px;background:var(--orange)}

/* hero */
.hero{left:0;top:105px;width:1200px;height:550px;background:linear-gradient(100deg,#7a6246 0%,#5b4a3a 35%,#3e3a36 65%,#2f2d2c 100%)}
.hero h1{position:absolute;left:632px;top:135px;font-size:52px;line-height:50px;font-weight:700;color:var(--white)}

/* section heading */
.h-section{position:absolute;width:1200px;text-align:center;font-size:38px;font-weight:600}
.rule{position:absolute;height:3px;width:36px;background:var(--orange)}

/* tabs */
.tabs{position:absolute;left:0;top:806px;width:1200px;display:flex;justify-content:center;font-size:12px;font-weight:500}
.tabs span{padding:0 18px;border-left:1px solid #ccc}
.tabs span:first-child{border-left:none;color:var(--orange);position:relative}
.tabs span:first-child::after{content:"";position:absolute;left:18px;right:18px;top:26px;height:3px;background:var(--orange)}

/* product cards */
.card{position:absolute;top:878px;width:232px;height:412px;background:var(--white);border:1px solid #ececec;border-radius:6px;box-shadow:0 2px 10px rgba(0,0,0,.08);overflow:hidden}
.card .photo{position:absolute;left:0;top:0;width:100%;height:186px;background:#f7f7f7}
.card .cone{position:absolute;left:92px;top:22px;width:48px;height:136px;border-radius:6px}
.card .corner{position:absolute;left:0;top:0;width:0;height:0;border-top:72px solid var(--yellow);border-right:72px solid transparent}
.card .corner-text{position:absolute;left:-2px;top:16px;transform:rotate(-45deg);font-size:7px;font-weight:600;line-height:8px;text-align:center;width:60px}
.card .brand{position:absolute;right:10px;top:14px;font-size:11px;font-weight:600;color:var(--ink);display:flex;align-items:center;gap:4px}
.card .brand i{display:block;width:10px;height:10px;background:var(--ink)}
.card .sku{position:absolute;left:50px;top:172px;width:132px;height:26px;border-radius:4px;background:var(--green-pill);color:var(--white);font-size:11px;font-weight:500;text-align:center;line-height:26px}
.card h3{position:absolute;left:0;top:210px;width:100%;text-align:center;font-size:12.5px;font-weight:600;line-height:15px}
.specs{position:absolute;left:8px;top:260px;width:214px;display:flex;gap:4px}
.specs div{flex:1;height:42px;border:1px solid var(--line);border-radius:3px;text-align:center;font-size:8px;padding-top:6px}
.specs b{display:block;font-weight:600;margin-bottom:8px}
.specs em{font-style:normal;color:#999}
.card .reviews{position:absolute;left:0;top:326px;width:100%;text-align:center;font-size:10px}
.stars{color:var(--orange);font-size:14px;letter-spacing:2px;display:block}
.card .btn{left:8px;top:372px;width:216px;height:32px;font-size:11px}
.arrow-circle{position:absolute;width:32px;height:32px;border-radius:50%;background:var(--white);box-shadow:0 1px 6px rgba(0,0,0,.2);display:flex;align-items:center;justify-content:center}

/* categories */
.categories{left:0;top:1361px;width:1200px;height:523px;background:linear-gradient(180deg,#73b35b,#65a94d)}
.cat{position:absolute;top:1524px;width:226px;height:226px;border-radius:50%;background:var(--yellow);border:5px solid #f9e27a}
.cat .img{position:absolute;left:21px;top:21px;width:174px;height:174px;border-radius:50%;border:4px solid #3a3a3a}
.cat-label{position:absolute;top:1770px;width:226px;text-align:center;color:var(--white);font-size:20px;font-weight:600}

/* about */
.about-ring{left:122px;top:1960px;width:452px;height:452px;border-radius:50%;background:var(--orange)}
.about-ring .img{position:absolute;left:46px;top:46px;width:360px;height:360px;border-radius:50%;border:8px solid var(--white);background:linear-gradient(135deg,#c9582a,#e57e2d 45%,#8cbe3e 70%,#b84b27)}
.about-title{left:630px;top:1992px;font-size:42px;line-height:46px;font-weight:600}
.about-text{left:630px;top:2117px;width:460px;font-size:11px;line-height:19px;color:#444}
.about-text p+p{margin-top:19px}

/* testimonials */
.testimonials{left:0;top:2493px;width:1200px;height:569px;background:var(--peach)}
.t-title{left:212px;top:2570px;font-size:38px;line-height:41px;font-weight:600}
.t-card{position:absolute;top:2705px;width:430px;height:264px;background:var(--white);border-radius:10px}
.avatar{position:absolute;left:42px;top:30px;width:72px;height:72px;border-radius:50%;background:var(--yellow);border:4px solid #f7e38a}
.avatar i{position:absolute;left:6px;top:6px;width:52px;height:52px;border-radius:50%;background:#c9b49a}
.t-card p{position:absolute;left:48px;top:124px;width:360px;font-size:10.5px;line-height:19px;color:#444}
.t-card .name{position:absolute;left:48px;top:232px;font-size:12px;font-weight:600}
.t-card .role{position:absolute;left:48px;top:248px;font-size:10px;color:var(--muted)}
.t-card .rate{position:absolute;right:20px;top:230px;font-size:10px;color:var(--muted);text-align:right}

/* contact */
.field-label{position:absolute;font-size:10px;font-weight:500;text-align:center;width:338px}
.field{position:absolute;border:1px solid #cfcfcf;border-radius:2px;font-size:10px;color:#aaa;text-align:center}

/* call band */
.call{left:0;top:3700px;width:1200px;height:208px;background:linear-gradient(90deg,#e9862e,#ef9841)}
.call h2{position:absolute;left:245px;top:71px;color:var(--white);font-size:34px;line-height:36px;font-weight:600}
.phone-box{position:absolute;left:627px;top:75px;width:363px;height:72px;border:2px solid #f6b77a;background:var(--orange-dark);color:var(--yellow);font-size:40px;font-weight:600;display:flex;align-items:center;justify-content:center;border-radius:4px}

/* footer */
.footer{left:0;top:3908px;width:1200px;height:311px;background:var(--footer);color:var(--white)}
.f-head{position:absolute;top:77px;font-size:11px;font-weight:600;color:var(--orange);letter-spacing:.5px}
.f-list{position:absolute;top:102px;font-size:10px;line-height:19px}
.circle-icon{position:absolute;width:32px;height:32px;border-radius:50%;background:#4a4a4a;border:1px solid #777}
.pay{position:absolute;top:4185px;width:30px;height:19px;border-radius:2px}
</style>
</head>
<body>

<header class="site-header">
  <div class="logo" style="left:110px;top:28px">
    <span class="logo-mark"></span>
    <span><span class="logo-name">Bluefinward</span><span class="logo-sub">Safety Products</span></span>
  </div>
  <div class="abs search">Enter keyword or item#
    <svg class="abs" style="right:12px;top:9px" width="14" height="14" viewBox="0 0 14 14"><circle cx="6" cy="6" r="4.5" fill="none" stroke="#555" stroke-width="1.4"/><line x1="9.3" y1="9.3" x2="13" y2="13" stroke="#555" stroke-width="1.4"/></svg>
  </div>
  <div class="btn" style="left:969px;top:10px;width:121px;height:34px;font-size:11px">Talk to us</div>
  <nav class="nav">
    <a class="active" style="left:487px">Home</a>
    <a style="left:560px">Products</a>
    <a style="left:649px">Industries</a>
    <a style="left:743px">Resources</a>
    <a style="left:910px;font-weight:400">US-EN</a>
    <a style="left:1010px">My Account ⌄</a>
  </nav>
  <svg class="abs" style="left:972px;top:62px" width="30" height="30" viewBox="0 0 30 30"><circle cx="15" cy="15" r="14" fill="#f3f3f3"/><circle cx="15" cy="12" r="4" fill="none" stroke="#c88a2e" stroke-width="1.4"/><path d="M8 22c1.5-4 12.5-4 14 0" fill="none" stroke="#c88a2e" stroke-width="1.4"/></svg>
</header>

<section class="abs hero" role="img" aria-label="Warehouse worker in hard hat driving a yellow forklift between shelving stacked with boxes">
  <h1>Manufacturer<br>of Traffic Control<br>and Personal<br>Safety Products</h1>
  <div class="btn" style="left:636px;top:367px;width:280px;height:36px;font-size:11px">Let's Go For The Shop Safety Product</div>
</section>

<h2 class="h-section" style="top:722px">Featuring <span class="accent">Safety Products</span></h2>
<div class="tabs"><span>Traffic Cones</span><span>Traffic Barriers</span><span>Mesh Signs</span><span>Safety Clothing</span></div>

<div class="arrow-circle" style="left:36px;top:1052px"><svg width="10" height="10" viewBox="0 0 10 10"><path d="M6.5 1.5 3 5l3.5 3.5" fill="none" stroke="#333" stroke-width="1.3"/></svg></div>
<div class="arrow-circle" style="left:1134px;top:1052px"><svg width="10" height="10" viewBox="0 0 10 10"><path d="M3.5 1.5 7 5 3.5 8.5" fill="none" stroke="#333" stroke-width="1.3"/></svg></div>

<article class="card" style="left:110px">
  <div class="photo"></div><div class="cone" role="img" aria-label="Orange traffic cone with two reflective collars" style="background:linear-gradient(180deg,#f07a2a,#e8581b)"></div>
  <div class="corner"></div><div class="corner-text">2 Reflective<br>Collars</div>
  <div class="brand"><i></i>Conewell</div>
  <div class="sku">2810064B</div>
  <h3>28" 10lb Orange Cone<br>w/(2) Lumax Reflective Collars</h3>
  <div class="specs"><div><b>Height</b><em>28"</em></div><div><b>Base</b><em>15"</em></div><div><b>Weight</b><em>10 LB</em></div><div><b>Color</b><em>Orange</em></div></div>
  <div class="reviews">4.6 Based on 100+ Rateway reviews<span class="stars">★★★★★</span></div>
  <div class="btn">SHOP NOW</div>
</article>
<article class="card" style="left:358px">
  <div class="photo"></div><div class="cone" role="img" aria-label="Lime traffic cone with two reflective collars" style="background:linear-gradient(180deg,#c6e83a,#8fc21c)"></div>
  <div class="corner"></div><div class="corner-text">2 Reflective<br>Collars</div>
  <div class="brand"><i></i>Ridgeway</div>
  <div class="sku">287L64B</div>
  <h3>28" 7lb Lime Cone w/(2)<br>Lumax Reflective Collars</h3>
  <div class="specs"><div><b>Height</b><em>28"</em></div><div><b>Base</b><em>15"</em></div><div><b>Weight</b><em>07 LB</em></div><div><b>Color</b><em>Lime</em></div></div>
  <div class="reviews">4.6 Based on 100+ Rateway reviews<span class="stars">★★★★★</span></div>
  <div class="btn">SHOP NOW</div>
</article>
<article class="card" style="left:607px">
  <div class="photo"></div><div class="cone" role="img" aria-label="Red traffic cone without collars" style="background:linear-gradient(180deg,#f05a2a,#d9391a)"></div>
  <div class="corner"></div><div class="corner-text">No Reflective<br>Collars</div>
  <div class="brand"><i></i>Markline</div>
  <div class="sku">2810064B</div>
  <h3>28" 10lb Orange Cone<br>w/(2) Lumax Reflective Collars</h3>
  <div class="specs"><div><b>Height</b><em>28"</em></div><div><b>Base</b><em>15"</em></div><div><b>Weight</b><em>10 LB</em></div><div><b>Color</b><em>Red</em></div></div>
  <div class="reviews">4.6 Based on 100+ Rateway reviews<span class="stars">★★★★★</span></div>
  <div class="btn">SHOP NOW</div>
</article>
<article class="card" style="left:857px">
  <div class="photo"></div><div class="cone" role="img" aria-label="Orange traffic cone with two reflective collars" style="background:linear-gradient(180deg,#f07a2a,#e8581b)"></div>
  <div class="corner"></div><div class="corner-text">2 Reflective<br>Collars</div>
  <div class="brand"><i></i>Poststar</div>
  <div class="sku">2810064B</div>
  <h3>28" 10lb Orange Cone<br>w/(2) Lumax Reflective Collars</h3>
  <div class="specs"><div><b>Height</b><em>28"</em></div><div><b>Base</b><em>15"</em></div><div><b>Weight</b><em>10 LB</em></div><div><b>Color</b><em>Orange</em></div></div>
  <div class="reviews">4.6 Based on 100+ Rateway reviews<span class="stars">★★★★★</span></div>
  <div class="btn">SHOP NOW</div>
</article>

<section class="abs categories" role="img" aria-label="Green-tinted photo of road workers and traffic cones"></section>
<h2 class="h-section" style="top:1432px;color:var(--white)">Top Selling Categories</h2>
<div class="rule" style="left:582px;top:1492px"></div>
<div class="cat" style="left:112px"><div class="img" role="img" aria-label="Stacked orange traffic cones" style="background:linear-gradient(160deg,#6f7b86,#e4692a 55%,#f1f1f1)"></div></div>
<div class="cat" style="left:361px"><div class="img" role="img" aria-label="Road lined with orange traffic barriers" style="background:linear-gradient(160deg,#9fb4c6,#d06a3a 55%,#7c7c7c)"></div></div>
<div class="cat" style="left:611px"><div class="img" role="img" aria-label="Orange diamond flagger warning sign" style="background:linear-gradient(160deg,#333,#e8561c 50%,#3b3b3b)"></div></div>
<div class="cat" style="left:862px"><div class="img" role="img" aria-label="Worker wearing an orange high-visibility jacket" style="background:linear-gradient(160deg,#4f4f4f,#f0802a 60%,#d2d2d2)"></div></div>
<div class="cat-label" style="left:112px">Traffic Cones</div>
<div class="cat-label" style="left:361px">Traffic Barriers</div>
<div class="cat-label" style="left:611px">Mesh Signs</div>
<div class="cat-label" style="left:862px">Safety Clothing</div>

<div class="abs about-ring"><div class="img" role="img" aria-label="Close-up of orange reflective safety vests"></div></div>
<h2 class="abs about-title"><span class="accent">Bluefinward</span><br>Safety Products</h2>
<div class="rule" style="left:630px;top:2093px"></div>
<div class="abs about-text">
  <p>Lorem ipsum dolor sit amet, consectetur adipiscing elit. Duis laoreet, massa vel auctor varius, neque lectus mollis massa, vel ornare leo augue accumsan neque. Aliquam tempus semper felis, in pulvinar neque bibendum vel. In dictum nibh purus, sit amet blandit elit laoreet eget. Mauris ut varius ligula, sed gravida justo. Suspendisse potenti. Phasellus interdum nulla in nisi gravida, nec feugiat lectus accumsan. Donec blandit diam non ante facilisis, sed bibendum eros fermentum.</p>
  <p>Lorem ipsum dolor sit amet, consectetur adipiscing elit. Duis laoreet, massa vel auctor varius, neque lectus mollis massa, vel ornare leo augue accumsan neque. Aliquam tempus semper felis, in pulvinar</p>
</div>
<div class="btn" style="left:630px;top:2338px;width:127px;height:38px;font-size:11px;background:var(--green)">Talk to us</div>

<section class="abs testimonials"></section>
<h2 class="abs t-title">What's Customer<br>Are Saying <span class="accent">About Us...</span></h2>
<div class="rule" style="left:212px;top:2666px"></div>
<div class="arrow-circle" style="left:86px;top:2818px;width:48px;height:48px;background:var(--orange)"><svg width="14" height="14" viewBox="0 0 14 14"><path d="M2.5 9 7 4.5 11.5 9" fill="none" stroke="#fff" stroke-width="1.6"/></svg></div>
<div class="arrow-circle" style="left:92px;top:2878px"><svg width="12" height="12" viewBox="0 0 12 12"><path d="M2 4.5 6 8.5 10 4.5" fill="none" stroke="#333" stroke-width="1.4"/></svg></div>
<div class="t-card" style="left:210px">
  <div class="avatar" role="img" aria-label="Customer portrait"><i></i></div>
  <p>Lorem ipsum dolor sit amet, consectetur adipiscing elit. Cras nec neque lectus. Duis id hendrerit eros. Cras condimentum arcu libero, a ultricies arcu ultricies vel. Praesent non porttitor arcu. Aliquam erat volutpat.</p>
  <div class="name">Marla Voss</div><div class="role">Manager</div>
  <div class="rate">4.6 Based on 100+ Rateway reviews<span class="stars">★★★★★</span></div>
</div>
<div class="t-card" style="left:660px">
  <div class="avatar" role="img" aria-label="Customer portrait"><i></i></div>
  <p>Lorem ipsum dolor sit amet, consectetur adipiscing elit. Cras nec neque lectus. Duis id hendrerit eros. Cras condimentum arcu libero, a ultricies arcu ultricies vel. Praesent non porttitor arcu. Aliquam erat volutpat.</p>
  <div class="name">Marla Voss</div><div class="role">Manager</div>
  <div class="rate">4.6 Based on 100+ Rateway reviews<span class="stars">★★★★★</span></div>
</div>

<h2 class="h-section" style="top:3140px">Get In Touch <span class="accent">With Us</span></h2>
<div class="field-label" style="left:255px;top:3236px">Your Name*</div>
<div class="field-label" style="left:605px;top:3236px">Phone Number*</div>
<div class="field" style="left:255px;top:3256px;width:338px;height:40px;line-height:38px">Michal whogan</div>
<div class="field" style="left:605px;top:3256px;width:338px;height:40px;line-height:38px">ex 123 456 7890</div>
<div class="field-label" style="left:255px;top:3323px">Email Address*</div>
<div class="field-label" style="left:605px;top:3323px">Company*</div>
<div class="field" style="left:255px;top:3343px;width:338px;height:40px;line-height:38px">mag@example.com</div>
<div class="field" style="left:605px;top:3343px;width:338px;height:40px;line-height:38px">Company</div>
<div class="field-label" style="left:430px;top:3410px">Message*</div>
<div class="field" style="left:255px;top:3430px;width:688px;height:128px;line-height:126px">Type Your message</div>
<div class="btn" style="left:523px;top:3590px;width:154px;height:38px;font-size:11px">Submit Now</div>

<section class="abs call">
  <h2>Call Us Today<br>For Any Question</h2>
  <div class="phone-box">123-456-7890</div>
</section>

<footer class="abs footer">
  <div class="f-head" style="left:211px">CONTACT US</div>
  <svg class="abs" style="left:211px;top:104px" width="12" height="16" viewBox="0 0 12 16"><path d="M6 0a6 6 0 0 0-6 6c0 4.5 6 10 6 10s6-5.5 6-10a6 6 0 0 0-6-6zm0 8.3A2.3 2.3 0 1 1 6 3.7a2.3 2.3 0 0 1 0 4.6z" fill="#fff"/></svg>
  <div class="f-list" style="left:232px;top:102px;line-height:14px">Location Name Will Be<br>Here</div>
  <svg class="abs" style="left:211px;top:150px" width="14" height="14" viewBox="0 0 14 14"><path d="M3 1l2 3-1.3 1.4c.8 1.9 2.1 3.2 4 4L9 8l3 2-1 3C5.5 13 1 8.5 1 3z" fill="#fff"/></svg>
  <div class="f-list" style="left:232px;top:145px;font-size:12px">0123456789</div>
  <svg class="abs" style="left:211px;top:181px" width="14" height="10" viewBox="0 0 14 10"><rect width="14" height="10" rx="1" fill="#f5c431"/><path d="M0 0l7 5 7-5" fill="none" stroke="#262626" stroke-width="1.2"/></svg>
  <div class="f-list" style="left:232px;top:176px;color:var(--yellow);text-decoration:underline">info@bluefinwardco.com</div>

  <div class="f-head" style="left:451px">SHOP</div>
  <div class="f-list" style="left:451px">SHOP PRODUCTS<br>SHOP BY APPLICATION<br>RESOURCES<br>QUOTE REQUEST</div>

  <div class="f-head" style="left:636px">COMPANY</div>
  <div class="f-list" style="left:636px">About Us<br>Contact Us<br>Privacy Policy<br>Returns<br>Terms &amp; Conditions</div>

  <div class="logo" style="left:812px;top:62px">
    <span class="logo-mark"></span>
    <span><span class="logo-name" style="font-size:22px">Bluefinward</span><span class="logo-sub" style="color:var(--white);font-size:10px">Safety Products</span></span>
  </div>
  <div class="f-head" style="left:820px;top:147px">FOLLOW US</div>
  <div class="circle-icon" style="left:818px;top:172px"></div>
  <div class="circle-icon" style="left:858px;top:172px"></div>
  <div class="circle-icon" style="left:898px;top:172px;background:var(--orange);border-color:var(--orange)"></div>
  <div class="circle-icon" style="left:938px;top:172px"></div>

  <div class="abs" style="left:211px;top:252px;width:780px;height:1px;background:#444"></div>
  <div class="abs" style="left:211px;top:268px;font-size:10px;color:#bbb">©2023 By Bluefinwardco.com</div>
</footer>
<div class="pay" style="left:852px;background:#e9eef7"></div>
<div class="pay" style="left:886px;background:#f3a23a"></div>
<div class="pay" style="left:920px;background:#d9423a"></div>
<div class="pay" style="left:954px;background:#5aa3dc"></div>

</body>
</html>
```